We need a business card design, letterhead design and envelope design for our corporate image

We are looking for a corporate business card design, letterhead and envelope design to match the business card design. Logo is done.

```html
<!DOCTYPE html>
<html lang="en">
<head>
<meta charset="utf-8">
<title>Velmora — Business Card</title>
<link rel="stylesheet" href="https://fonts.googleapis.com/css2?family=Montserrat:wght@400;500;600&family=Oswald:wght@500;600&display=swap">
<style>
  :root {
    --backdrop: #1c1c1c;
    --card: #262626;
    --card-edge: #2e2e2e;
    --accent: #f7c600;
    --text-light: #f2f2f2;
    --logo-grey: #9a9a9a;
  }
  * { margin: 0; padding: 0; box-sizing: border-box; }
  html, body {
    width: 1200px;
    height: 900px;
    overflow: hidden;
    background: var(--backdrop);
  }
  .canvas {
    width: 1200px;
    height: 900px;
    display: flex;
    flex-direction: column;
    align-items: center;
    justify-content: center;
    gap: 44px;
  }
  .card {
    position: relative;
    width: 680px;
    height: 380px;
    background: linear-gradient(135deg, var(--card-edge), var(--card));
    border-bottom: 6px solid var(--accent);
    box-shadow: 0 18px 40px rgba(0,0,0,0.55);
  }
  /* Front */
  .card-front {
    display: flex;
    align-items: center;
    justify-content: center;
  }
  .brand-name {
    font-family: "Montserrat", sans-serif;
    font-weight: 600;
    font-size: 64px;
    letter-spacing: -1px;
    color: var(--logo-grey);
  }
  /* Back */
  .card-back {
    display: flex;
    align-items: center;
    justify-content: center;
    gap: 30px;
  }
  .identity {
    text-align: right;
  }
  .person-name {
    font-family: "Oswald", sans-serif;
    font-weight: 600;
    font-size: 46px;
    line-height: 1;
    letter-spacing: 1px;
    color: var(--accent);
    text-transform: uppercase;
  }
  .person-role {
    margin-top: 6px;
    font-family: "Montserrat", sans-serif;
    font-weight: 400;
    font-size: 19px;
    letter-spacing: 1px;
    color: var(--text-light);
    text-transform: uppercase;
  }
  .divider {
    width: 2px;
    height: 100px;
    background: var(--accent);
  }
  .contact-list {
    list-style: none;
    display: flex;
    flex-direction: column;
    gap: 5px;
  }
  .contact-item {
    display: flex;
    align-items: center;
    gap: 10px;
    font-family: "Montserrat", sans-serif;
    font-weight: 500;
    font-size: 19px;
    color: var(--text-light);
  }
  .contact-icon {
    width: 14px;
    height: 14px;
    flex: none;
  }
</style>
</head>
<body>
<main class="canvas">
  <section class="card card-front">
    <span class="brand-name">Velmora</span>
  </section>

  <section class="card card-back">
    <div class="identity">
      <p class="person-name">Daniel Brooks</p>
      <p class="person-role">Director</p>
    </div>
    <span class="divider"></span>
    <ul class="contact-list">
      <li class="contact-item">
        <svg class="contact-icon" viewBox="0 0 16 16"><path d="M3.5 1.5l3 3-1.6 1.6a8 8 0 0 0 5 5l1.6-1.6 3 3-2 2C6 14 2 10 1.5 3.5z" fill="none" stroke="var(--accent)" stroke-width="1.5" stroke-linejoin="round"/></svg>
        +330 5172-4036
      </li>
      <li class="contact-item">
        <svg class="contact-icon" viewBox="0 0 16 16"><rect x="1.5" y="3.5" width="13" height="9" fill="none" stroke="var(--accent)" stroke-width="1.5"/><path d="M1.5 3.5L8 9l6.5-5.5" fill="none" stroke="var(--accent)" stroke-width="1.5"/></svg>
        hello@velmora.com
      </li>
      <li class="contact-item">
        <svg class="contact-icon" viewBox="0 0 16 16"><circle cx="8" cy="8" r="6.5" fill="none" stroke="var(--accent)" stroke-width="1.3"/><ellipse cx="8" cy="8" rx="3" ry="6.5" fill="none" stroke="var(--accent)" stroke-width="1.1"/><path d="M1.5 8h13M2.5 5h11M2.5 11h11" stroke="var(--accent)" stroke-width="1"/></svg>
        www.velmora.com
      </li>
      <li class="contact-item">
        <svg class="contact-icon" viewBox="0 0 16 16"><path d="M8 15s5-5.5 5-9A5 5 0 0 0 3 6c0 3.5 5 9 5 9z" fill="var(--accent)"/><circle cx="8" cy="6" r="1.8" fill="var(--card)"/></svg>
        Easton, PA USA
      </li>
    </ul>
  </section>
</main>
</body>
</html>
```